Banner required for our website Sale of Silent Domestic Rangehoods

These images around silence are very good however, even more important are the family conversations that happen within the kitchen area.
These conversations are often disrupted by the use of a noisy rangehood.
A Family photos in the kitchen with a tag line relating to regaining those precious moments would be a great concept.
Regards Neil
Just a few suggestions.
I would prefer no illistrations.
Most importantly I am still seeking a visual to highlite the silent benifit of our rangehoods.The best visual will most like win this contest. We currently use the lady with the finger held to her mouth. Any other suggestions would be greatly appreciated.
We need a banner ad for the sale of designer silent domestic rangehoods.
These rangehood are aimed at the middle to higher income buyers, they are Elegant, efficient and powerful.
We aim to offer a product that exceeds our customers expectations.
Visit our website and everything we do is self explainatory.
www.mirovale.com.au
Regards Neil
Updates
Mirovale Silent rangehoods enable the family to again enjoy conversations in the kitchen
You can have friends over, revel in each others company and enjoy a great lunch or dinner without the distraction of a rangehood that sounds like a jet engine.
They also simply work better
Our promo banners typically have 2 sizes: 500x500 pixels for our socials, and a 2570*730 pixels for our Promotions page
Target Market(s)
Renovators, second home buyers, ladies between 28 and 49 years of age
Requirements
Must have
- Appealing visuals, upmarket look and feel.
Nice to have
- Family picture with kids.
Should not have
- The words Cheap, Budget nor afforadable.

```html
<!DOCTYPE html>
<html lang="en">
<head>
<meta charset="utf-8">
<title>Mirovale – Silent Rangehood Banners</title>
<link rel="stylesheet" href="https://fonts.googleapis.com/css2?family=Roboto:wght@700&family=Nunito:wght@600;700&display=swap">
<style>
  :root {
    --magenta: #d90f6b;
    --magenta-soft: rgba(217, 15, 107, 0.94);
    --white: #ffffff;
    --ring-grey: #efefef;
    --dot-pink: #f4b8d2;
    --page: #ffffff;
  }
  html, body {
    margin: 0;
    padding: 0;
    width: 1200px;
    height: 654px;
    overflow: hidden;
    background: var(--page);
  }
  .canvas {
    position: relative;
    width: 1200px;
    height: 654px;
  }

  /* Promotions page banner */
  .promo-banner {
    position: absolute;
    left: 40px;
    top: 38px;
    width: 1120px;
    height: 318px;
    overflow: hidden;
    box-shadow: 0 3px 8px rgba(0,0,0,0.25);
  }
  .promo-banner__scene {
    position: absolute;
    inset: 0;
    background:
      radial-gradient(ellipse 260px 200px at 640px 250px, rgba(190,140,115,0.85), rgba(190,140,115,0) 70%),
      radial-gradient(ellipse 220px 180px at 800px 260px, rgba(150,160,200,0.6), rgba(150,160,200,0) 70%),
      linear-gradient(180deg, rgba(0,0,0,0) 55%, rgba(235,235,235,0.55) 100%),
      linear-gradient(90deg, #8a92a3 0%, #a4abb9 30%, #7c8494 46%, #2f3440 56%, #3a3f4a 66%, #5a5f6a 74%, #e7e9e4 84%, #f1f2ee 94%, #dcdeda 100%);
  }
  .promo-banner__panel {
    position: absolute;
    left: 114px;
    top: 0;
    width: 309px;
    height: 100%;
    background: var(--magenta-soft);
  }
  .promo-banner__product {
    position: absolute;
    left: 118px;
    top: 0;
    width: 187px;
    height: 96px;
    background: linear-gradient(180deg, #c4c7ca 0%, #e3e5e7 60%, #d0d3d6 100%);
  }
  .brand-name {
    font-family: 'Nunito', sans-serif;
    font-weight: 700;
    color: var(--white);
    margin: 0;
  }
  .promo-banner__brand {
    position: absolute;
    left: 41px;
    top: 53px;
    font-size: 12px;
    line-height: 14px;
  }
  .headline {
    font-family: 'Roboto', sans-serif;
    font-weight: 700;
    margin: 0;
    letter-spacing: -0.5px;
  }
  .promo-banner__headline {
    position: absolute;
    left: 37px;
    top: 92px;
    font-size: 56px;
    line-height: 55px;
    color: var(--white);
  }
  .promo-banner__cta {
    position: absolute;
    left: 39px;
    top: 274px;
    width: 104px;
    height: 21px;
    border: 1px solid var(--white);
    font-family: 'Nunito', sans-serif;
    font-weight: 600;
    font-size: 10px;
    color: var(--white);
    display: flex;
    align-items: center;
    justify-content: center;
  }

  /* Social square */
  .social-square {
    position: absolute;
    left: 40px;
    top: 398px;
    width: 218px;
    height: 218px;
    overflow: hidden;
    box-shadow: 0 3px 8px rgba(0,0,0,0.25);
  }
  .social-square__shapes {
    position: absolute;
    inset: 0;
  }
  .social-square__brand {
    position: absolute;
    left: 110px;
    top: 5px;
    width: 64px;
    height: 15px;
    background: var(--magenta);
    font-size: 10.5px;
    line-height: 15px;
    text-align: center;
  }
  .social-square__headline {
    position: absolute;
    left: 8px;
    top: 64px;
    font-size: 17.5px;
    line-height: 20.5px;
    color: var(--magenta);
  }
  .social-square__cta {
    position: absolute;
    left: 10px;
    top: 132px;
    width: 65px;
    height: 17px;
    background: var(--magenta);
    font-family: 'Nunito', sans-serif;
    font-weight: 600;
    font-size: 7px;
    color: var(--white);
    display: flex;
    align-items: center;
    justify-content: center;
  }
</style>
</head>
<body>
<main class="canvas">

  <section class="promo-banner">
    <div class="promo-banner__scene" role="img" aria-label="Photo of a family in a bright kitchen: a father holding a toddler beside a smiling mother, with grey cabinets, a chimney rangehood and a white fridge behind them"></div>
    <div class="promo-banner__panel">
      <div class="promo-banner__product" role="img" aria-label="Product photo of a stainless steel island rangehood"></div>
      <p class="brand-name promo-banner__brand">mirovale</p>
      <h1 class="headline promo-banner__headline">Silent.<br>Powerful.<br>Beautiful.</h1>
      <div class="promo-banner__cta">Discover Silence</div>
    </div>
  </section>

  <section class="social-square">
    <svg class="social-square__shapes" width="218" height="218" viewBox="0 0 218 218">
      <defs>
        <linearGradient id="familyTones" x1="0" y1="0" x2="1" y2="1">
          <stop offset="0" stop-color="#3b3f48"/>
          <stop offset="0.55" stop-color="#a98472"/>
          <stop offset="1" stop-color="#e2ded8"/>
        </linearGradient>
      </defs>
      <rect width="218" height="218" fill="var(--magenta)"/>
      <circle cx="140" cy="110" r="138" fill="var(--white)"/>
      <circle cx="140" cy="110" r="118" fill="none" stroke="#f8d3e3" stroke-width="0.6"/>
      <circle cx="47" cy="47" r="1.6" fill="var(--dot-pink)"/>
      <circle cx="202" cy="15" r="1.6" fill="var(--dot-pink)"/>
      <circle cx="44" cy="167" r="1.6" fill="var(--dot-pink)"/>
      <circle cx="201" cy="205" r="1.6" fill="var(--dot-pink)"/>
      <path d="M 105 205 A 100 100 0 0 0 218 150" fill="none" stroke="var(--magenta)" stroke-width="15"/>
      <circle cx="142" cy="114" r="78" fill="none" stroke="var(--ring-grey)" stroke-width="16"/>
      <circle cx="142" cy="114" r="62" fill="url(#familyTones)" role="img" aria-label="Photo of a family cooking together in a kitchen with a recipe book"/>
      <line x1="195" y1="53" x2="87" y2="166" stroke="var(--magenta)" stroke-width="1.2"/>
    </svg>
    <p class="brand-name social-square__brand">mirovale</p>
    <h2 class="headline social-square__headline">Silent.<br>Powerful.<br>Beautiful.</h2>
    <div class="social-square__cta">Discover Silence</div>
  </section>

</main>
</body>
</html>
```